South bound Billboard quorvin- Hot Deli Advertise

We have a hot deli that has pizza made from scratch, Mesquite smoked ribs, pop corn chicken and more inside our C-Store. We have been serving food in our store for over 30 years and have a full kitchen open from 4am -10pm. Want some creative ways to catch customers eyes and get them to stop at our C-Store! I have put a picture of the billboard I am getting redone would like to keep the quorvin side the same but moved to the left side and get creative with the right side.
Target Market(s)
People driving looking for a one stop shop
Requirements
Must have
- look sharp and professional
Nice to have
- Pictures that make you hungry

```html
<!DOCTYPE html>
<html lang="en">
<head>
<meta charset="utf-8">
<title>Mesa Ridge Food Mart – Hot Deli Billboard</title>
<link href="https://fonts.googleapis.com/css2?family=Poppins:wght@400;500;600;700;800&display=swap" rel="stylesheet">
<style>
  :root {
    --navy: #1c2433;
    --wood: #2d2c2b;
    --wood-dark: #232221;
    --orange: #e5833c;
    --yellow: #f1c04f;
    --ink: #121722;
    --crust: #e2c79c;
    --crust-dark: #b88a55;
    --sauce: #c23a26;
    --cheese: #efe1c3;
    --mushroom: #8a7560;
    --basil: #3f7a2e;
    --chicken: #d99a45;
    --chicken-dark: #a8672a;
    --carton: #c7302b;
  }
  * { box-sizing: border-box; margin: 0; padding: 0; }
  html, body { width: 1200px; height: 801px; overflow: hidden; background: #ffffff; }
  .billboard {
    position: relative;
    width: 1200px;
    height: 801px;
    overflow: hidden;
    background: repeating-linear-gradient(180deg, var(--wood) 0 78px, var(--wood-dark) 78px 81px);
    font-family: "Poppins", sans-serif;
  }
  .brand-panel { position: absolute; inset: 0; width: 100%; height: 100%; }

  .brand-name {
    position: absolute;
    left: 70px; top: 110px;
    width: 440px;
    padding: 28px 20px 30px;
    background: var(--orange);
    border-radius: 16px;
    color: var(--ink);
    text-align: center;
    font-weight: 800;
    line-height: 1;
  }
  .brand-mark {
    display: block;
    width: 24px; height: 24px;
    margin: 0 auto 16px;
    border-radius: 50%;
    background: var(--ink);
  }
  .brand-main { display: block; font-size: 60px; letter-spacing: 1px; }
  .brand-sub { display: block; font-size: 28px; margin-top: 12px; letter-spacing: 4px; }

  .hours-band {
    position: absolute;
    left: 60px; top: 400px;
    width: 460px; height: 130px;
    background: var(--orange);
    transform: rotate(3deg);
    display: flex; align-items: center; justify-content: center;
    color: var(--ink);
    font-weight: 700;
    font-size: 78px;
    letter-spacing: -1px;
    white-space: nowrap;
  }

  .contact {
    position: absolute;
    left: 90px; top: 590px;
    width: 420px;
    transform: rotate(3deg);
  }
  .delivery-note {
    text-align: right;
    color: var(--orange);
    font-size: 20px;
    font-weight: 500;
    letter-spacing: 1.5px;
  }
  .phone {
    margin-top: 4px;
    color: var(--yellow);
    font-weight: 600;
    font-size: 36px;
    letter-spacing: 1px;
    white-space: nowrap;
  }

  .pizza-photo {
    position: absolute;
    left: 585px; top: 150px;
    width: 430px; height: 560px;
    border-radius: 50%;
    transform: rotate(-10deg);
    background:
      radial-gradient(ellipse at 38% 35%, rgba(63,122,46,.55) 0 4%, transparent 9%),
      radial-gradient(ellipse at 62% 58%, rgba(63,122,46,.5) 0 4%, transparent 9%),
      radial-gradient(ellipse at 55% 30%, rgba(194,58,38,.7) 0 6%, transparent 12%),
      radial-gradient(ellipse at 40% 65%, rgba(194,58,38,.7) 0 6%, transparent 12%),
      radial-gradient(ellipse at 50% 50%, var(--cheese) 0 20%, var(--mushroom) 45%, var(--sauce) 62%, var(--crust) 74%, var(--crust-dark) 86%, rgba(184,138,85,0) 71%);
    box-shadow: 0 18px 40px rgba(0,0,0,.45);
  }
  .years-badge {
    position: absolute;
    left: 950px; top: 150px;
    width: 235px; height: 120px;
    background: var(--yellow);
    transform: rotate(3deg);
    display: flex; align-items: center; justify-content: center;
    color: var(--ink);
    font-weight: 700;
    font-size: 44px;
    white-space: nowrap;
  }
  .chicken-photo {
    position: absolute;
    left: 960px; top: 560px;
    width: 210px; height: 210px;
    border-radius: 40% 14px 40% 30%;
    background:
      radial-gradient(circle at 30% 65%, var(--chicken) 0 22%, transparent 40%),
      radial-gradient(circle at 55% 80%, var(--chicken-dark) 0 18%, transparent 36%),
      linear-gradient(135deg, var(--chicken) 0 45%, var(--carton) 70% 100%);
    box-shadow: 0 12px 28px rgba(0,0,0,.4);
  }
</style>
</head>
<body>
  <main class="billboard">
    <svg class="brand-panel" viewBox="0 0 1200 801" aria-hidden="true">
      <path d="M0 0 H500 C560 90 600 220 570 330 C545 430 600 560 565 801 H0 Z" fill="var(--navy)"/>
    </svg>

    <div class="brand-name">
      <span class="brand-mark"></span>
      <span class="brand-main">MESA RIDGE</span>
      <span class="brand-sub">FOOD MART</span>
    </div>

    <div class="hours-band">4am -10pm</div>

    <div class="contact">
      <p class="delivery-note">FREE DELIVERY</p>
      <p class="phone">0147 - 258 - 369</p>
    </div>

    <div class="pizza-photo" role="img" aria-label="Photo of a scratch-made pizza topped with red peppers, mushrooms, cherry tomatoes and fresh spinach"></div>
    <div class="years-badge">30 years</div>
    <div class="chicken-photo" role="img" aria-label="Photo of golden popcorn chicken spilling from a red striped carton"></div>
  </main>
</body>
</html>
```